Mine Engineering Consultancy specializing in
* Pit optimization
* Mine Design
* Scheduling
* Mine Rehabilitation

Mining

RVT Mining Pty Ltd
Dennis Holloway
Director/Principle Mining Engineer
Mobile 0418263591
Email dennis.holloway@rvtmining-example.com

```html
<!DOCTYPE html>
<html lang="en">
<head>
<meta charset="utf-8">
<title>RVT Mining Pty Ltd — Business Cards</title>
<link rel="stylesheet" href="https://fonts.googleapis.com/css2?family=Cormorant+Garamond:wght@400;500&family=Lato:wght@400;700&family=Exo+2:wght@600&display=swap">
<style>
  :root {
    --backdrop: #c9cccd;
    --card-light: #dde1e4;
    --brand-blue: #1c5fa3;
    --navy-deep: #141e5e;
    --navy-mid: #26348a;
    --paper: #f1f1f3;
    --ink-white: #eef0f6;
  }
  * { box-sizing: border-box; margin: 0; padding: 0; }
  html, body { width: 1200px; height: 871px; overflow: hidden; }
  body {
    background: var(--backdrop);
    display: flex;
    align-items: center;
    justify-content: center;
    gap: 40px;
    font-family: "Lato", sans-serif;
  }
  .card {
    position: relative;
    width: 540px;
    height: 320px;
    overflow: hidden;
    box-shadow: 0 6px 18px rgba(0,0,0,0.18);
  }

  /* Back card: services */
  .card--services { background: var(--card-light); }
  .brand-tile {
    position: absolute;
    top: 28px; right: 40px;
    width: 190px; height: 120px;
    background: var(--paper);
    display: flex; align-items: center; justify-content: center;
    box-shadow: inset 0 0 10px rgba(0,0,0,0.12);
  }
  .brand-tile__name {
    font-family: "Cormorant Garamond", serif;
    font-weight: 500;
    font-size: 26px;
    color: var(--brand-blue);
  }
  .brand-caption {
    position: absolute;
    top: 156px; right: 40px;
    width: 190px;
    text-align: right;
    font-family: "Cormorant Garamond", serif;
    font-size: 22px;
    color: var(--brand-blue);
  }
  .services {
    position: absolute;
    left: 0; bottom: 36px;
    width: 300px;
    padding: 16px 18px 16px 24px;
    background: var(--brand-blue);
    color: #fff;
    font-weight: 700;
    font-size: 15px;
    line-height: 1.3;
  }
  .services ul { list-style: none; }
  .services li::before { content: "- "; }

  /* Front card: contact */
  .card--contact {
    background: radial-gradient(ellipse at 70% 55%, var(--navy-mid), var(--navy-deep) 75%);
  }
  .card__photo { position: absolute; inset: 0; }
  .identity {
    position: absolute;
    top: 30px; left: 40px;
    color: var(--ink-white);
  }
  .identity__company {
    font-family: "Cormorant Garamond", serif;
    font-size: 24px;
    margin-bottom: 8px;
  }
  .identity__person { font-weight: 700; font-size: 13px; line-height: 1.35; }
  .contact-strip {
    position: absolute;
    right: 0; top: 150px;
    width: 300px;
    padding: 10px 16px;
    background: var(--paper);
    font-family: "Exo 2", sans-serif;
    font-weight: 600;
    font-size: 13px;
    line-height: 1.35;
    color: var(--brand-blue);
  }
  .contact-strip__email { font-size: 12px; }
  .brand-large {
    position: absolute;
    left: 36px; bottom: 28px;
    font-family: "Cormorant Garamond", serif;
    font-weight: 500;
    font-size: 58px;
    color: var(--ink-white);
  }
</style>
</head>
<body>

  <section class="card card--services">
    <div class="brand-tile"><span class="brand-tile__name">RVT Mining</span></div>
    <p class="brand-caption">RVT Mining Pty Ltd</p>
    <div class="services">
      <p>Mine Engineering Consultancy<br>specializing in:</p>
      <ul>
        <li>Pit optimization</li>
        <li>Mine Design</li>
        <li>Scheduling</li>
        <li>Mine Rehabilitation</li>
      </ul>
    </div>
  </section>

  <section class="card card--contact">
    <div class="card__photo" role="img" aria-label="Aerial photograph of an open-pit mine with haul roads, toned deep navy blue"></div>
    <div class="identity">
      <p class="identity__company">RVT Mining Pty Ltd</p>
      <p class="identity__person">Dennis Holloway<br>Director/Principle Mining Engineer</p>
    </div>
    <div class="contact-strip">
      <p>0418263591</p>
      <p class="contact-strip__email">dennis.holloway@rvtmining-example.com</p>
    </div>
    <p class="brand-large">RVT Mining</p>
  </section>

</body>
</html>
```